401K Retirement Plan Consultant

Professional & clean lines - not overly busy. We offer two services - 401k administration and HSA administration. Based on the outskirts of Charlotte NC. Communicate the services we offer along with the financial institutions that we work with. Mixture of icons and people pictures.

Current website - tvh401k.com,
It is presently very amateurish.

```html
<!DOCTYPE html>
<html lang="en">
<head>
<meta charset="utf-8">
<title>TVH401k Employee Benefits</title>
<link href="https://fonts.googleapis.com/css2?family=Montserrat:wght@600;700;800&family=Roboto:wght@300;400;500;700&display=swap" rel="stylesheet">
<style>
:root{
  --blue:#1d14c7;
  --green:#47ad4b;
  --green-light:#5bbb5e;
  --ink:#1b1b1b;
  --text:#5c5c5c;
  --grey-bg:#f3f3f3;
  --footer:#1e1e1e;
  --white:#ffffff;
}
*{box-sizing:border-box;margin:0;padding:0}
html,body{width:1200px;height:3394px;overflow:hidden}
body{font-family:"Roboto",sans-serif;color:var(--text);background:var(--white);position:relative}
.abs{position:absolute}
.btn{display:inline-flex;align-items:center;gap:10px;background:var(--green);color:var(--white);font-family:"Roboto",sans-serif;font-weight:500;font-size:15px;letter-spacing:.3px;text-transform:uppercase;height:39px;padding:0 22px;text-decoration:none}
.btn svg{width:15px;height:15px}
.heading{font-family:"Montserrat",sans-serif;font-weight:800;color:var(--ink);font-size:37px;letter-spacing:.5px}
.heading-rule{width:88px;height:4px;background:var(--blue);margin-top:6px}

/* header */
.site-header{top:0;left:0;width:1200px;height:75px;background:var(--white)}
.brand{font-family:"Montserrat",sans-serif;font-weight:700;font-size:30px;color:var(--ink);line-height:1}
.brand-sub{font-family:"Roboto",sans-serif;font-size:10.5px;letter-spacing:2.4px;color:var(--ink);margin-top:3px}
.site-header .brand-wrap{left:144px;top:14px}
.nav{left:455px;top:27px;display:flex;gap:47px;font-family:"Roboto",sans-serif;font-weight:500;font-size:14px;color:#222}
.nav .active{color:var(--ink);border-bottom:3px solid var(--blue);padding-bottom:6px}
.call{left:893px;top:14px;display:flex;gap:12px;align-items:center}
.call-icon{width:38px;height:38px;border-radius:50%;background:var(--blue);display:flex;align-items:center;justify-content:center}
.call small{display:block;font-size:11.5px;color:#444}
.call strong{display:block;font-size:16px;color:var(--ink);font-weight:700;margin-top:2px}

/* hero */
.hero{top:75px;left:0;width:1200px;height:560px;background:linear-gradient(100deg,#8a6a3c 0%,#a7904c 35%,#6f7b3a 65%,#4e5c2b 100%)}
.hero h1{left:144px;top:165px;font-family:"Montserrat",sans-serif;font-weight:800;font-size:40px;color:var(--white);letter-spacing:.5px}
.hero h1 span{color:var(--blue)}
.hero p{left:145px;top:223px;width:420px;font-size:15.5px;line-height:27px;color:var(--white)}
.hero .btn{left:145px;top:307px;height:46px;padding:0 24px}
.dots{left:575px;top:515px;display:flex;gap:8px}
.dots i{width:11px;height:11px;border-radius:50%;border:2px solid var(--white);display:block}
.dots i.on{background:var(--green);border-color:var(--green)}

/* about */
.about-back{left:209px;top:714px;width:328px;height:349px;background:linear-gradient(180deg,#2a6fd1 0%,#6f9ed8 40%,#a9b7c5 100%)}
.about-front{left:145px;top:775px;width:328px;height:335px;background:linear-gradient(135deg,#c9c6c4,#7a6a63 55%,#d7cfcb);border:5px solid var(--white);box-shadow:0 2px 8px rgba(0,0,0,.15)}
.about-copy{left:620px;top:728px;width:434px}
.about-copy p{font-size:13.2px;line-height:24px;color:var(--text);margin-top:16px;text-align:justify}
.about-copy p.first{margin-top:30px}
.about-copy .btn{margin-top:28px}

/* features */
.features{top:1192px;left:0;width:1200px;height:800px;background:var(--grey-bg)}
.feature{width:296px;text-align:center}
.feature .icon{width:82px;height:82px;border-radius:50%;background:var(--blue);margin:0 auto;display:flex;align-items:center;justify-content:center}
.feature .icon svg{width:44px;height:44px}
.feature h3{font-family:"Roboto",sans-serif;font-weight:500;font-size:17.5px;color:var(--ink);margin-top:22px}
.feature p{font-size:12.8px;line-height:21px;color:var(--text);margin:14px 14px 0}
.feature.highlight{background:var(--white);border-bottom:5px solid var(--green);box-shadow:0 4px 18px rgba(0,0,0,.08);padding-top:37px;height:293px}
.feature.highlight .icon{background:var(--green)}

/* services */
.services-band{top:1992px;left:0;width:1200px;height:468px;background:linear-gradient(180deg,var(--green-light),var(--green))}
.services-title{top:2053px;left:0;width:1200px;text-align:center}
.services-title .heading{color:var(--white)}
.services-title .heading-rule{margin:6px auto 0}
.services-intro{top:2140px;left:100px;width:1000px;text-align:center;color:var(--white);font-size:14.5px;line-height:24px}
.service-card{top:2246px;width:439px;height:461px;background:var(--white);border-radius:12px;box-shadow:0 6px 16px rgba(0,0,0,.16);text-align:center;padding:6px}
.service-card .photo{height:211px;border-radius:8px 8px 0 0}
.service-card .badge{width:70px;height:70px;border-radius:50%;background:var(--blue);border:4px solid var(--white);margin:-35px auto 0;position:relative;display:flex;align-items:center;justify-content:center}
.service-card .badge svg{width:36px;height:36px}
.service-card h3{font-family:"Roboto",sans-serif;font-weight:500;font-size:17px;color:var(--ink);margin-top:18px;letter-spacing:.3px}
.service-card p{font-size:13.5px;line-height:21px;color:var(--text);margin:14px 24px 0}
.service-card .btn{margin-top:26px}

/* partners */
.partners-title{top:2785px;left:0;width:1200px;text-align:center}
.partners-title .heading-rule{margin:6px auto 0}
.partner{top:2898px;width:214px;height:76px;display:flex;align-items:center;justify-content:center;font-family:"Roboto",sans-serif;font-weight:500;font-size:22px;background:var(--white)}
.partner.boxed{box-shadow:0 2px 12px rgba(0,0,0,.1);border-radius:4px}
.arrow{top:2918px}

/* footer */
.site-footer{top:3082px;left:0;width:1200px;height:312px;background:var(--footer);color:var(--white)}
.site-footer .brand,.site-footer .brand-sub{color:var(--white)}
.footer-col h4{font-family:"Roboto",sans-serif;font-weight:700;font-size:14.5px;letter-spacing:.2px}
.footer-col ul{list-style:none;margin-top:14px}
.footer-col li{font-size:11px;line-height:25px}
.socials{display:flex;gap:14px}
.socials i{width:11px;height:11px;border-radius:50%;background:var(--white);display:block}
.newsletter p{font-size:11px;line-height:19px;margin-top:14px;width:310px}
.subscribe{display:flex;margin-top:16px;width:300px;height:41px;border:2px solid var(--white)}
.subscribe span{flex:1;background:var(--white);color:#666;font-size:11px;display:flex;align-items:center;padding-left:16px}
.subscribe b{width:112px;background:var(--green);display:flex;align-items:center;justify-content:center;font-size:13px}
.copyright{top:3350px;left:0;width:1200px;text-align:center;font-size:12px;color:var(--white)}
</style>
</head>
<body>

<header class="abs site-header">
  <div class="abs brand-wrap"><div class="brand">TVH401k</div><div class="brand-sub">EMPLOYEE BENEFITS</div></div>
  <nav class="abs nav"><span class="active">HOME</span><span>ABOUT US</span><span>SERVICES</span><span>CONTACT US</span></nav>
  <div class="abs call">
    <div class="call-icon"><svg width="20" height="20" viewBox="0 0 24 24" fill="#fff"><path d="M6.6 10.8a15.1 15.1 0 0 0 6.6 6.6l2.2-2.2a1 1 0 0 1 1-.25 11.4 11.4 0 0 0 3.6.57 1 1 0 0 1 1 1V20a1 1 0 0 1-1 1A17 17 0 0 1 3 4a1 1 0 0 1 1-1h3.5a1 1 0 0 1 1 1c0 1.25.2 2.45.57 3.57a1 1 0 0 1-.25 1z"/></svg></div>
    <div><small>Call Us Now</small><strong>1 704 555 0142</strong></div>
  </div>
</header>

<section class="abs hero" role="img" aria-label="Photo of a family running hand in hand along a sunny meadow path">
  <h1 class="abs">WELCOME TO TVH<span>401K</span></h1>
  <p class="abs">Located in the heart of Cedar Cove, SC, TVH has been providing employee benefits since 1987.</p>
  <a class="abs btn">GET STARTED <svg viewBox="0 0 16 16" fill="none" stroke="#fff" stroke-width="2"><path d="M2 8h11M9 4l4 4-4 4"/></svg></a>
  <div class="abs dots"><i class="on"></i><i></i><i></i></div>
</section>

<div class="abs about-back" role="img" aria-label="Photo of glass office towers against a blue sky"></div>
<div class="abs about-front" role="img" aria-label="Photo of a happy family lying together and laughing"></div>
<div class="abs about-copy">
  <h2 class="heading">ABOUT US</h2>
  <div class="heading-rule"></div>
  <p class="first">Located in the heart of Cedar Cove, SC, TVH has been providing employee benefits since 1987. We specialize in small companies normally with les than 150 employees.TVH's retirement plan solutions are designed to serve a broad range of clients and offer the advantages of large-plan pricing to small employer-sponsored retirement plans.</p>
  <p>Setting up an employee retirement plan can be a smart way to provide for one of your key assets – your people.</p>
  <a class="btn">LEARN MORE <svg viewBox="0 0 16 16" fill="none" stroke="#fff" stroke-width="2"><path d="M2 8h11M9 4l4 4-4 4"/></svg></a>
</div>

<section class="abs features"></section>

<div class="abs feature" style="left:122px;top:1260px">
  <div class="icon"><svg viewBox="0 0 44 44" fill="none" stroke="#fff" stroke-width="2"><rect x="16" y="4" width="12" height="9"/><rect x="4" y="30" width="10" height="9"/><rect x="17" y="30" width="10" height="9"/><rect x="30" y="30" width="10" height="9"/><path d="M22 13v9M9 30v-8h26v8M22 22v8"/></svg></div>
  <h3>Open Architecture Platform</h3>
  <p>All of our plans are designed using an open architecture investment platform. This allows for a myriad of investment choices for its participants.</p>
</div>
<div class="abs feature" style="left:449px;top:1260px">
  <div class="icon"><svg viewBox="0 0 44 44" fill="none" stroke="#fff" stroke-width="2"><circle cx="22" cy="10" r="5"/><path d="M22 15v7M10 28v-6h24v6"/><path d="M6 30l4-3 4 3v5l-4 3-4-3zM18 30l4-3 4 3v5l-4 3-4-3zM30 30l4-3 4 3v5l-4 3-4-3z"/></svg></div>
  <h3>Employer Allocation Preparation</h3>
  <p>Calculation of Employer Matching and/or Profit Sharing Contribution using various allocation methods.</p>
</div>
<div class="abs feature" style="left:775px;top:1260px">
  <div class="icon"><svg viewBox="0 0 44 44" fill="none" stroke="#fff" stroke-width="2"><circle cx="19" cy="11" r="6"/><path d="M7 40V27a7 7 0 0 1 7-7h10a7 7 0 0 1 6 3"/><rect x="25" y="29" width="14" height="10"/><path d="M29 29v-3h6v3M14 28v12"/></svg></div>
  <h3>Employee Education</h3>
  <p>TVH401k provides participants with group educational meetings to discuss plan features, investment options, which helps your participants be better prepared</p>
</div>

<div class="abs feature" style="left:122px;top:1580px">
  <div class="icon"><svg viewBox="0 0 44 44" fill="none" stroke="#fff" stroke-width="2"><rect x="6" y="10" width="26" height="28"/><path d="M11 18h12M11 24h8M11 30h12"/><path d="M28 28l10-16 3 2-10 16-4 2z"/></svg></div>
  <h3>Plan Design &amp; Document Services</h3>
  <p>Preparation of the Volume Submitter document, adoption agreement and all required forms and notices.  These plans are pre-approved by the Internal</p>
</div>
<div class="abs feature highlight" style="left:449px;top:1542px">
  <div class="icon"><svg viewBox="0 0 44 44" fill="none" stroke="#fff" stroke-width="2"><rect x="8" y="6" width="12" height="14"/><rect x="24" y="24" width="12" height="14"/><path d="M20 12h10v8M24 31H14v-8"/><path d="M10 28h4M30 16h4"/></svg></div>
  <h3>Non-Discrimination Testing</h3>
  <p>Nondiscrimination tests ensure that highly compensated employees do not take substantially greater advantage of this tax savings than lower-paid employees.</p>
</div>
<div class="abs feature" style="left:775px;top:1580px">
  <div class="icon"><svg viewBox="0 0 44 44" fill="none" stroke="#fff" stroke-width="2"><circle cx="22" cy="12" r="7"/><path d="M8 40v-6a12 12 0 0 1 24-4"/><circle cx="16" cy="34" r="4"/><path d="M16 27v3M16 38v3M9 34h3M20 34h3"/></svg></div>
  <h3>COBRA Administration</h3>
  <p>This is the federal law that provides many workers with the right to continue coverage in a group health plan. This federal law applies to employers with 20</p>
</div>

<a class="abs btn" style="left:530px;top:1881px">VIEW MORE <svg viewBox="0 0 16 16" fill="none" stroke="#fff" stroke-width="2"><path d="M2 8h11M9 4l4 4-4 4"/></svg></a>

<section class="abs services-band"></section>
<div class="abs services-title"><h2 class="heading">OUR SERVICES</h2><div class="heading-rule"></div></div>
<p class="abs services-intro">Most people realize that, we all have to accept more responsibility for saving for our own retirement.  It's widely accepted that Social Security is only meant to provide a modest percentage of your retirement income<br>So Social Security alone will not be enough</p>

<article class="abs service-card" style="left:145px">
  <div class="photo" role="img" aria-label="Photo of business colleagues gathered around a laptop in an office" style="background:linear-gradient(135deg,#cfd3d8,#6b6f78 50%,#e4e4e4)"></div>
  <div class="badge"><svg viewBox="0 0 36 36" fill="none" stroke="#fff" stroke-width="1.8"><circle cx="18" cy="14" r="9"/><circle cx="18" cy="14" r="3"/><path d="M8 34a10 10 0 0 1 20 0"/></svg></div>
  <h3>401K ADMINISTRATION</h3>
  <p>Lorem ipsum dolor sit amet, consectetur adipiscing elit, sed do eiusmod tempor incididunt ut labore et dolore magna aliqua. Ut enim ad minim veniam, quis nostrud exercitation.</p>
  <a class="btn">LEARN MORE <svg viewBox="0 0 16 16" fill="none" stroke="#fff" stroke-width="2"><path d="M2 8h11M9 4l4 4-4 4"/></svg></a>
</article>
<article class="abs service-card" style="left:616px">
  <div class="photo" role="img" aria-label="Photo of a team reviewing documents together at a desk" style="background:linear-gradient(135deg,#8d8a86,#4b4a4f 50%,#c8c2ba)"></div>
  <div class="badge"><svg viewBox="0 0 36 36" fill="none" stroke="#fff" stroke-width="1.8"><circle cx="18" cy="8" r="4"/><path d="M18 12v6M8 24v-6h20v6"/><circle cx="8" cy="28" r="3"/><circle cx="18" cy="28" r="3"/><circle cx="28" cy="28" r="3"/></svg></div>
  <h3>HSA ADMINISTRATION</h3>
  <p>Lorem ipsum dolor sit amet, consectetur adipiscing elit, sed do eiusmod tempor incididunt ut labore et dolore magna aliqua. Ut enim ad minim veniam, quis nostrud exercitation.</p>
  <a class="btn">LEARN MORE <svg viewBox="0 0 16 16" fill="none" stroke="#fff" stroke-width="2"><path d="M2 8h11M9 4l4 4-4 4"/></svg></a>
</article>

<div class="abs partners-title"><h2 class="heading">OUR PARTNERS</h2><div class="heading-rule"></div></div>
<svg class="abs arrow" style="left:88px" width="22" height="36" viewBox="0 0 22 36" fill="none" stroke="#888" stroke-width="3"><path d="M18 3L4 18l14 15"/></svg>
<div class="abs partner" style="left:137px;color:#e5761e">Vantra Financial</div>
<div class="abs partner boxed" style="left:377px;color:#1e2f6b">Emberline</div>
<div class="abs partner boxed" style="left:609px;color:#2a54b8">Alvora</div>
<div class="abs partner" style="left:855px;color:#555">Westmark Klein</div>
<svg class="abs arrow" style="left:1091px" width="22" height="36" viewBox="0 0 22 36" fill="none" stroke="#888" stroke-width="3"><path d="M4 3l14 15L4 33"/></svg>

<footer class="abs site-footer">
  <div class="abs" style="left:144px;top:80px"><div class="brand">TVH401k</div><div class="brand-sub">EMPLOYEE BENEFITS</div></div>
  <div class="abs socials" style="left:163px;top:154px" aria-label="Social links"><i></i><i></i><i></i><i></i></div>
  <div class="abs footer-col" style="left:387px;top:60px"><h4>COMPANY</h4><ul><li>Home</li><li>About Us</li><li>Services</li><li>Contact Us</li></ul></div>
  <div class="abs footer-col" style="left:561px;top:60px"><h4>INFORMATION</h4><ul><li>Privacy Policy</li><li>Terms of Use</li><li>Site map</li></ul></div>
  <div class="abs footer-col newsletter" style="left:757px;top:60px"><h4>SUBSCRIBE TO OUR NEWSLETTER</h4><p>Contact us today to request a custom fee comparison or a quote for a startup plan.  It's quick and easy.</p><div class="subscribe"><span>Email Address</span><b>SUBSCRIBE</b></div></div>
</footer>
<p class="abs copyright">Copy Rights ©  TVH 401k 2024 | Allrights Reserved</p>

</body>
</html>
```